Design Footer or Header for Pizza Restaurant Menu

-Design a footer or header using our logo and contact information.
-The menu items in the middle should be exactly as shown in the .psd examples.
-2 Pages (both should have the same design of Footer or Header)
-Menu Items (Document Link)
https://sheets.brindlework.com/tables/d/7QpXa2mR9vLt4KwZ8nHc3YeB6uJf1DsG5oNi0TzWr2Kx/edit?usp=sharing
Contact Information
8157 Tarrowell Avenue, Brennick Heights, NY 10477
847-318-5037
Ovenbellhub.com

```html
<!DOCTYPE html>
<html lang="en">
<head>
<meta charset="utf-8">
<title>Ovenbell Pizza Menu</title>
<link href="https://fonts.googleapis.com/css2?family=Arimo:wght@400;700&family=Oswald:wght@500&display=swap" rel="stylesheet">
<style>
:root{
  --red:#e3171f;
  --ink:#1a1a1a;
  --muted:#6a6a6a;
  --paper:#f7f6f1;
  --wood-light:#f1f1f0;
  --wood-dark:#d9d9d8;
  --rule:#bdbdbd;
}
*{margin:0;padding:0;box-sizing:border-box}
html,body{width:1200px;height:932px;overflow:hidden;background:#fff}
body{position:relative;font-family:'Arimo',Arial,sans-serif;color:var(--ink)}
.page{position:absolute;top:58px;width:518px;height:808px;background:var(--paper);box-shadow:0 2px 8px rgba(0,0,0,.25);overflow:hidden}
.page--food{left:51px}
.page--pizza{left:624px}
.header{position:absolute;left:0;top:0;width:100%;height:170px}
.header__texture{position:absolute;inset:0;background:linear-gradient(160deg,var(--wood-light),var(--wood-dark) 60%,var(--wood-light))}
.header__wave,.footer__wave{position:absolute;left:0;width:100%}
.header__wave{bottom:0;height:60px}
.footer{position:absolute;left:0;bottom:0;width:100%;height:34px}
.footer__texture{position:absolute;inset:0;background:linear-gradient(160deg,var(--wood-dark),var(--wood-light))}
.footer__wave{top:0;height:34px}
.brand{position:absolute;left:0;right:0;top:52px;display:flex;justify-content:center;align-items:center;gap:8px}
.brand__name{font-family:'Arimo',sans-serif;font-weight:700;font-size:38px;color:var(--ink);letter-spacing:-.5px}
.brand__dot{width:22px;height:22px;border-radius:50%;background:var(--red)}
.contact{position:absolute;font-size:8.5px;line-height:11px;color:var(--red);text-transform:uppercase;letter-spacing:.2px}
.contact--address{left:8px;top:80px}
.contact--phone{right:9px;top:83px;font-size:10px;line-height:13px;text-align:right}
.page--pizza .contact--address{top:68px}
.page--pizza .contact--phone{top:73px}
.section{position:absolute}
.section__title{color:var(--red);font-size:11px;text-align:center;padding-bottom:6px;border-bottom:1px solid var(--rule);margin-bottom:7px;font-weight:400;letter-spacing:.3px}
.section__note{display:block;font-size:5px;margin-top:1px}
.item{margin-bottom:4px}
.item__line{display:flex;align-items:baseline;font-size:8.3px;line-height:9px;text-transform:uppercase}
.item__dots{flex:1;border-bottom:1px dotted #666;margin:0 1px;transform:translateY(-2px)}
.item__price{white-space:nowrap}
.item__price small{font-size:4.5px}
.item__desc{font-size:5.6px;line-height:6.4px;color:var(--muted);text-transform:uppercase}
.col-l{left:6px;width:247px}
.col-r{left:263px;width:247px}
.pz-l{left:6px;width:249px}
.pz-r{left:261px;width:251px}
.appetizers .item{margin-bottom:6px}
.entrees .item{margin-bottom:3px}
.pizza .item{margin-bottom:5px}
.toppings .item{margin-bottom:7.8px}
.desserts .item{margin-bottom:11.5px}
.desserts .item__desc{font-size:7.6px;line-height:8px;color:var(--ink)}
.special{position:absolute;left:265px;top:372px;width:245px;height:74px;border:1.5px solid var(--red);border-radius:5px;background:#fff;text-align:center}
.special__title{font-family:'Oswald',sans-serif;color:var(--red);font-size:11px;margin-top:2px;letter-spacing:.4px}
.special__sub{font-size:5.8px;margin:1px 0 5px}
.special__prices{font-family:'Oswald',sans-serif;font-size:11.5px;letter-spacing:1.2px;line-height:16px}
.special__prices sup{font-size:5.5px}
.special__note{font-size:5px}
.addons{position:absolute;left:6px;top:728px;width:247px;display:flex;justify-content:space-around;text-align:center;font-size:5.2px;line-height:6.4px;text-transform:uppercase}
.addons__title{color:var(--red);font-weight:700;font-size:6px;margin-bottom:3px}
.addons__col + .addons__col{border-left:1px solid #999;padding-left:18px}
</style>
</head>
<body>

<!-- ===== Page 1: starters, panini, salads, entrees ===== -->
<section class="page page--food">
  <header class="header">
    <div class="header__texture" role="img" aria-label="Light grey wood texture with faint line drawings of cooking ingredients"></div>
    <svg class="header__wave" viewBox="0 0 518 60" preserveAspectRatio="none" aria-hidden="true">
      <path d="M0 42 C120 10 260 40 380 20 C440 10 490 22 518 38 L518 60 L0 60Z" fill="#222"/>
      <path d="M0 40 C120 8 260 36 380 16 C440 6 490 18 518 32 L518 48 C490 30 440 20 380 28 C260 46 120 22 0 50Z" fill="var(--red)"/>
      <path d="M0 50 C120 22 260 46 380 28 C440 20 490 30 518 48 L518 60 L0 60Z" fill="var(--paper)"/>
    </svg>
    <div class="brand"><span class="brand__name">Ovenbell</span><span class="brand__dot"></span></div>
    <p class="contact contact--address">8157 Tarrowell Avenue,<br>Brennick Heights,<br>NY 10477</p>
    <p class="contact contact--phone">847-318-5037<br>Ovenbellhub.com</p>
  </header>

  <div class="section col-l appetizers" style="top:177px">
    <h2 class="section__title">APPETIZERS</h2>
    <div class="item"><div class="item__line">Homemade Mozzarella Sticks (5)<span class="item__dots"></span><span class="item__price">$10.50</span></div><p class="item__desc">Smoked mozzarella chunky sticks coated in breadcrumbs served with spicy tomato sauce</p></div>
    <div class="item"><div class="item__line">Homemade Chicken Nuggets (6)<span class="item__dots"></span><span class="item__price">$9.50</span></div><p class="item__desc">Real homemade chicken nuggets (local farm raised chicken) served w/ french fries</p></div>
    <div class="item"><div class="item__line">Roasted Chicken Wings (6) (12)<span class="item__dots"></span><span class="item__price">$9.00/$16.00</span></div><p class="item__desc">Seasoned available in our homemade buffalo sauce, garlic &amp; romano cheese, hickory smoked bbq, honey bbq, cajun dry rub, sweet chili sauce</p></div>
    <div class="item"><div class="item__line">Polpette (Meatballs) (5)<span class="item__dots"></span><span class="item__price">$10.50</span></div><p class="item__desc">Homemade baked meatballs in rich tomato sauce with whipped buffalo ricotta</p></div>
    <div class="item"><div class="item__line">Firecracker Calamari<span class="item__dots"></span><span class="item__price">$14.00</span></div><p class="item__desc">Crispy fried calamari with cherry peppers served with lemon aioli and marinara (your choice of spicy &amp; not spicy)</p></div>
    <div class="item"><div class="item__line">Crocchette di Patate (5)<span class="item__dots"></span><span class="item__price">$9.50</span></div><p class="item__desc">Homemade potato croquettes filled w/ smoked mozzarella</p></div>
    <div class="item"><div class="item__line">Arancini (5)<span class="item__dots"></span><span class="item__price">$12.50</span></div><p class="item__desc">Sourdough crumbed rice balls with mixed wild mushrooms grana padano and gorgonzola emulsion</p></div>
    <div class="item"><div class="item__line">Charred Brussels Sprouts<span class="item__dots"></span><span class="item__price">$10.50</span></div><p class="item__desc">Brussels sprouts with crispy parmesan flakes</p></div>
    <div class="item"><div class="item__line">Homemade Fries<span class="item__dots"></span><span class="item__price">$8.50</span></div><p class="item__desc">House cut fries w/ your choice: classic, cajun spice or parmesan &amp; truffle</p></div>
    <div class="item"><div class="item__line">Garlic Bread with Cheese<span class="item__dots"></span><span class="item__price">$6.50</span></div><p class="item__desc">Homemade garlic bread on fresh Valtorre Italian bread w/ side of marinara</p></div>
  </div>

  <div class="section col-l" style="top:480px">
    <h2 class="section__title">SALADS</h2>
    <div class="item"><div class="item__line">The Market Bowl<span class="item__dots"></span><span class="item__price">$15.00</span></div><p class="item__desc">Romaine, tomatoes, corn, chickpeas, cucumbers, red onions, beets, carrots, avocado, pumpkin seeds, gorgonzola, shallot vinaigrette</p></div>
    <div class="item"><div class="item__line">Sweet Greens<span class="item__dots"></span><span class="item__price">$14.00</span></div><p class="item__desc">Arugula, apples, walnuts, goat cheese, onion, red wine vinaigrette</p></div>
    <div class="item"><div class="item__line">The Caesar<span class="item__dots"></span><span class="item__price">$12.00</span></div><p class="item__desc">Romaine, garlic croutons, parmesan, caesar dressing</p></div>
    <div class="item"><div class="item__line">Huskers Harvest<span class="item__dots"></span><span class="item__price">$14.00</span></div><p class="item__desc">Shaved kale, shaved brussels sprouts, rainbow quinoa, carrots, cucumbers, sunflower seeds, red onions, dried cranberries, avocado, champagne vinaigrette</p></div>
    <div class="item"><div class="item__line">Un-Feta-Getable Bowl<span class="item__dots"></span><span class="item__price">$14.00</span></div><p class="item__desc">Romaine, cucumbers, tomatoes, onions, kalamata olives, feta, greek dressing</p></div>
    <div class="item"><div class="item__line">Go Green<span class="item__dots"></span><span class="item__price">$14.00</span></div><p class="item__desc">Spring greens, fennel, celery, pears, toasted almonds, basil, shaved parmesan, cracked pepper, olive oil, citrus vinaigrette</p></div>
    <div class="item"><div class="item__line">Avo-Cobbo Bowl<span class="item__dots"></span><span class="item__price">$14.00</span></div><p class="item__desc">Romaine, tomatoes, cucumbers, chopped egg, avocado, red onions, shallot vinaigrette</p></div>
    <div class="item"><div class="item__line">Midwest Foodie Bowl<span class="item__dots"></span><span class="item__price">$14.00</span></div><p class="item__desc">Romaine, corn, beans, pico de gallo, jack, avocado, chipotle ranch</p></div>
  </div>
  <div class="addons">
    <div class="addons__col"><p class="addons__title">Toppings- $6<sup>00</sup></p><p>Grilled chicken<br>Breaded chicken cutlet<br>Cajun chicken</p></div>
    <div class="addons__col"><p class="addons__title">Toppings- $7<sup>00</sup></p><p>Grilled shrimp<br>Cajun shrimp<br>Salmon<br>Sliced skirt steak</p></div>
  </div>

  <div class="section col-r" style="top:173px">
    <h2 class="section__title">PANINI OR WRAPS<span class="section__note">(SERVED WITH PICKLE &amp; FRIES)</span></h2>
    <div class="item"><div class="item__line">Burrata, Pesto, Tomatoes<span class="item__dots"></span><span class="item__price">$12.00</span></div><p class="item__desc">Tomatoes, basil pesto, burrata, arugula, olive oil, cracked salt and pepper, balsamic reduction</p></div>
    <div class="item"><div class="item__line">Kickin' Cauliflower<span class="item__dots"></span><span class="item__price">$12.00</span></div><p class="item__desc">Crispy buffalo cauliflower, garlic sauteed kale, provolone, pickled jalapenos, garlic aioli</p></div>
    <div class="item"><div class="item__line">King Caesar<span class="item__dots"></span><span class="item__price">$14.00</span></div><p class="item__desc">Cajun chicken, romaine, parmesan, caesar dressing</p></div>
    <div class="item"><div class="item__line">Sca-More-Za Please!<span class="item__dots"></span><span class="item__price">$14.00</span></div><p class="item__desc">Caramelized onions, olives, basil, campari tomato, scamorza, evoo</p></div>
    <div class="item"><div class="item__line">The Sizzler<span class="item__dots"></span><span class="item__price">$14.00</span></div><p class="item__desc">Chicken cutlet, bacon, fresh mozzarella, jalapenos, vodka sauce</p></div>
    <div class="item"><div class="item__line">Not Cluckin' Around<span class="item__dots"></span><span class="item__price">$14.00</span></div><p class="item__desc">Grilled chicken, monterey jack, avocado, tomato, pesto aioli</p></div>
    <div class="item"><div class="item__line">Great Bambino<span class="item__dots"></span><span class="item__price">$14.00</span></div><p class="item__desc">Grilled chicken, prosciutto, fresh mozzarella, tomatoes pesto aioli</p></div>
  </div>

  <div class="special">
    <p class="special__title">PARMIGIANA &amp; MILANESE</p>
    <p class="special__sub">Milanese Style: Baby Arugula, Red Onion, Tomato, Shaved Parmigiano, Aged Balsamic</p>
    <p class="special__prices">CHICKEN $28<sup>75</sup> • JUMBO SHRIMP $33<sup>75</sup><br>EGGPLANT $28<sup>75</sup></p>
    <p class="special__note">Substitute Vodka Sauce $5<sup>25</sup></p>
  </div>

  <div class="section col-r entrees" style="top:480px">
    <h2 class="section__title">ENTREES</h2>
    <div class="item"><div class="item__line">Spaghetti Pesto alla Pollo<span class="item__dots"></span><span class="item__price">$19.50</span></div><p class="item__desc">Sauteed chicken breast, creamy basil pesto sauce &amp; parmesan</p></div>
    <div class="item"><div class="item__line">Pasta w/ Meatballs<span class="item__dots"></span><span class="item__price">$16.00</span></div><p class="item__desc">Pasta w/ homemade meatballs &amp; marinara sauce</p></div>
    <div class="item"><div class="item__line">Eggplant Parmigiana<span class="item__dots"></span><span class="item__price">$16.00</span></div><p class="item__desc">Nicely battered eggplant, marinara, mozzarella with side of spaghetti</p></div>
    <div class="item"><div class="item__line">Penne Vodka<span class="item__dots"></span><span class="item__price">$16.00</span></div><p class="item__desc">Touch of cream, tomato sauce, splash of vodka</p></div>
    <div class="item"><div class="item__line">Chicken Franchaise<span class="item__dots"></span><span class="item__price">$19.50</span></div><p class="item__desc">Lightly flour battered chicken breast sauteed in lemon white wine broth</p></div>
    <div class="item"><div class="item__line">Chicken Parmigiana<span class="item__dots"></span><span class="item__price">$18.50</span></div><p class="item__desc">Breaded chicken cutlet, smokey tomato sauce, parmesan and mozzarella over spaghetti</p></div>
    <div class="item"><div class="item__line">Chicken Scarpariello<span class="item__dots"></span><span class="item__price">$20.00</span></div><p class="item__desc">Chicken with italian sausage, olives, capers, mushrooms, and lightly spiced tomato sauce over honey garlic mashed potatoes</p></div>
    <div class="item"><div class="item__line">Classic Shrimp Scampi<span class="item__dots"></span><span class="item__price">$21.50</span></div><p class="item__desc">Shrimp scampi with fresh arugula, diced tomatoes, splash of lemon</p></div>
    <div class="item"><div class="item__line">Lasagna<span class="item__dots"></span><span class="item__price">$16.50</span></div><p class="item__desc">Our take on an italian classic</p></div>
    <div class="item"><div class="item__line">Roasted Faroe Island Salmon<span class="item__dots"></span><span class="item__price">$25.50</span></div><p class="item__desc">Cherry tomatoes, capers, kalamata olives, marinara over sauteed veggies</p></div>
    <div class="item"><div class="item__line">Thinly Sliced Skirt Steak<span class="item__dots"></span><span class="item__price">$25.50</span></div><p class="item__desc">Served with smokey slaw, crispy polenta, and chimichurri</p></div>
    <div class="item"><div class="item__line">32-Hour Slow Roasted Short Rib<span class="item__dots"></span><span class="item__price">$25.50</span></div><p class="item__desc">Glazed cherry tomatoes with roasted potatoes and fresh rosemary</p></div>
  </div>

  <footer class="footer">
    <div class="footer__texture" role="img" aria-label="Light grey wood texture with faint line drawings of cooking ingredients"></div>
    <svg class="footer__wave" viewBox="0 0 518 34" preserveAspectRatio="none" aria-hidden="true">
      <path d="M0 0 L518 0 L518 14 C440 20 360 6 260 8 C160 10 70 24 0 14Z" fill="var(--paper)"/>
      <path d="M0 14 C70 24 160 10 260 8 C360 6 440 20 518 14 L518 18 C440 24 360 11 260 13 C160 15 70 28 0 20Z" fill="var(--red)"/>
      <path d="M0 20 C70 28 160 15 260 13 C360 11 440 24 518 18 L518 20 C440 26 360 14 260 16 C160 18 70 30 0 23Z" fill="#222"/>
    </svg>
  </footer>
</section>

<!-- ===== Page 2: pizza, toppings, desserts ===== -->
<section class="page page--pizza">
  <header class="header">
    <div class="header__texture" role="img" aria-label="Light grey wood texture with faint line drawings of cooking ingredients"></div>
    <svg class="header__wave" viewBox="0 0 518 60" preserveAspectRatio="none" aria-hidden="true">
      <path d="M0 30 C100 20 200 44 320 34 C420 26 480 18 518 22 L518 60 L0 60Z" fill="#222"/>
      <path d="M0 26 C100 16 200 40 320 30 C420 22 480 14 518 18 L518 30 C480 26 420 34 320 42 C200 52 100 30 0 38Z" fill="var(--red)"/>
      <path d="M0 38 C100 30 200 52 320 42 C420 34 480 26 518 30 L518 60 L0 60Z" fill="var(--paper)"/>
    </svg>
    <div class="brand" style="top:44px"><span class="brand__name">Ovenbell</span><span class="brand__dot"></span></div>
    <p class="contact contact--address">8157 Tarrowell Avenue,<br>Brennick Heights,<br>NY 10477</p>
    <p class="contact contact--phone">847-318-5037<br>Ovenbellhub.com</p>
  </header>

  <div class="section pz-l pizza" style="top:186px">
    <h2 class="section__title">PIZZA</h2>
    <div class="item"><div class="item__line">The Big Cheese<span class="item__dots"></span><span class="item__price">$17.00<small>LARGE</small>/14.00<small>PER</small></span></div><p class="item__desc">Classic new york pizza, topped with tomato sauce and mozzarella</p></div>
    <div class="item"><div class="item__line">Hot Stuff<span class="item__dots"></span><span class="item__price">$21.00<small>LARGE</small>/15.00<small>PER</small></span></div><p class="item__desc">Chicken cutlet marinated in hot sauce, topped with homemade ranch dressing drizzle</p></div>
    <div class="item"><div class="item__line">BBQ Special<span class="item__dots"></span><span class="item__price">$21.00<small>LARGE</small>/15.00<small>PER</small></span></div><p class="item__desc">Chicken cutlet marinated in tangy barbeque sauce</p></div>
    <div class="item"><div class="item__line">Pizza Margherita<span class="item__dots"></span><span class="item__price">$21.00<small>LARGE</small>/15.00<small>PER</small></span></div><p class="item__desc">Margherita style pizza - topped with san marzano tomatoes, basil, mozzarella and olive oil drizzle</p></div>
    <div class="item"><div class="item__line">Great White<span class="item__dots"></span><span class="item__price">$21.00<small>LARGE</small>/15.00<small>PER</small></span></div><p class="item__desc">Battered eggplant coated in homemade tomato sauce, mozzarella, parmesan and ricotta</p></div>
    <div class="item"><div class="item__line">Eggplant Delight<span class="item__dots"></span><span class="item__price">$21.00<small>LARGE</small>/15.00<small>PER</small></span></div><p class="item__desc">Classic new york pizza, topped with tomato sauce and mozzarella</p></div>
    <div class="item"><div class="item__line">Chicken Club<span class="item__dots"></span><span class="item__price">$21.00<small>LARGE</small>/15.00<small>PER</small></span></div><p class="item__desc">Breaded chicken cutlet coated in homemade tomato sauce, mozzarella, parmesan and ricotta</p></div>
    <div class="item"><div class="item__line">Classic Chicken Francese<span class="item__dots"></span><span class="item__price">$21.00<small>LARGE</small>/15.00<small>PER</small></span></div><p class="item__desc">Battered chicken breast sauteed in lemon white wine broth</p></div>
    <div class="item"><div class="item__line">Hot Links<span class="item__dots"></span><span class="item__price">$22.00<small>LARGE</small>/16.00<small>PER</small></span></div><p class="item__desc">Crumbled hot sausage and vodka sauce</p></div>
    <div class="item"><div class="item__line">Ulti-Meat<span class="item__dots"></span><span class="item__price">$22.00<small>LARGE</small>/16.00<small>PER</small></span></div><p class="item__desc">Mozzarella, pastrami, salami, meatballs, creamy ricotta, chives, hot sausage, basil, caramelized onions, hot peppers</p></div>
    <div class="item"><div class="item__line">The Prosciutto*<span class="item__dots"></span><span class="item__price">$22.00<small>LARGE</small>/16.00<small>PER</small></span></div><p class="item__desc">Prosciutto di parma, arugula, fresh mozzarella</p></div>
    <div class="item"><div class="item__line">Get Em to the Greek!<span class="item__dots"></span><span class="item__price">$22.00<small>LARGE</small>/16.00<small>PER</small></span></div><p class="item__desc">Red onions, tomatoes, aromatic oregano, greek olives, feta cheese</p></div>
    <div class="item"><div class="item__line">Veggie Supreme*<span class="item__dots"></span><span class="item__price">$22.00<small>LARGE</small>/16.00<small>PER</small></span></div><p class="item__desc">Tomatoes, smoked mozzarella, seasonal vegetables, olives capers, evoo</p></div>
    <div class="item"><div class="item__line">Ricotta Be Kidding Me!<span class="item__dots"></span><span class="item__price">$22.00<small>LARGE</small>/16.00<small>PER</small></span></div><p class="item__desc">Ricotta, roasted garlic, charred baby broccoli, fresh mozzarella</p></div>
    <div class="item"><div class="item__line">Lots of Shrooms*<span class="item__dots"></span><span class="item__price">$22.00<small>LARGE</small>/16.00<small>PER</small></span></div><p class="item__desc">Fresh mozzarella, cream of mushrooms, mushrooms, arugula, truffle oil, parmesan</p></div>
    <div class="item"><div class="item__line">Pizza My Heart<span class="item__dots"></span><span class="item__price">$22.00<small>LARGE</small>/16.00<small>PER</small></span></div><p class="item__desc">Zucchini squash, artichoke hearts, garlic, fresh basil, oil, shaved parmesan</p></div>
    <div class="item"><div class="item__line">Veggiemore*<span class="item__dots"></span><span class="item__price">$22.00<small>LARGE</small>/16.00<small>PER</small></span></div><p class="item__desc">Eggplant, zucchini, roasted peppers, fresh mozzarella, san marzano tomato sauce</p></div>
    <div class="item"><div class="item__line">Shrimp Pancetta*<span class="item__dots"></span><span class="item__price">$22.00<small>LARGE</small>/16.00<small>PER</small></span></div><p class="item__desc">Shrimp, pancetta, arugula, fresh mozzarella, shaved parmesan, balsamic reduction</p></div>
    <div class="item"><div class="item__line">Bell-Cilian<span class="item__dots"></span><span class="item__price">$19.00<small>LARGE</small></span></div><p class="item__desc">Traditional thick crust sicilian style topped with tomato sauce and mozzarella</p></div>
    <div class="item"><div class="item__line">Grandma Pie<span class="item__dots"></span><span class="item__price">$23.00<small>LARGE</small></span></div><p class="item__desc">Thin crust topped with marinated tomato, fresh mozzarella, basil and garlic</p></div>
    <div class="item"><div class="item__line">Drunken Grandma<span class="item__dots"></span><span class="item__price">$23.00<small>LARGE</small></span></div><p class="item__desc">Crispy grandma style, topped with vodka sauce, fresh mozzarella, romano and fresh basil</p></div>
  </div>

  <div class="section pz-r toppings" style="top:186px">
    <h2 class="section__title">PIZZA TOPPINGS</h2>
    <div class="item"><div class="item__line">The Big Cheese<span class="item__dots"></span><span class="item__price">$4.50</span></div></div>
    <div class="item"><div class="item__line">Anchovies<span class="item__dots"></span><span class="item__price">$4.50</span></div></div>
    <div class="item"><div class="item__line">Artichoke Hearts<span class="item__dots"></span><span class="item__price">$4.50</span></div></div>
    <div class="item"><div class="item__line">Bacon<span class="item__dots"></span><span class="item__price">$4.50</span></div></div>
    <div class="item"><div class="item__line">Black Olives<span class="item__dots"></span><span class="item__price">$4.50</span></div></div>
    <div class="item"><div class="item__line">Broccoli<span class="item__dots"></span><span class="item__price">$4.50</span></div></div>
    <div class="item"><div class="item__line">Egg Plant<span class="item__dots"></span><span class="item__price">$4.50</span></div></div>
    <div class="item"><div class="item__line">Extra Cheese<span class="item__dots"></span><span class="item__price">$4.50</span></div></div>
    <div class="item"><div class="item__line">Fresh Garlic<span class="item__dots"></span><span class="item__price">$4.50</span></div></div>
    <div class="item"><div class="item__line">Fresh Mushrooms<span class="item__dots"></span><span class="item__price">$4.50</span></div></div>
    <div class="item"><div class="item__line">Green Peppers<span class="item__dots"></span><span class="item__price">$4.50</span></div></div>
    <div class="item"><div class="item__line">Hot Cherry Peppers<span class="item__dots"></span><span class="item__price">$4.50</span></div></div>
  </div>

  <div class="section pz-r desserts" style="top:452px">
    <h2 class="section__title">DESSERTS</h2>
    <div class="item"><div class="item__line">Plain Nocciella Crepe<span class="item__dots"></span><span class="item__price">$9.00</span></div></div>
    <div class="item"><div class="item__line">Banana +<span class="item__dots"></span><span class="item__price">$4.50</span></div><p class="item__desc">Fire roasted marshmello &amp; nocciella</p></div>
    <div class="item"><div class="item__line">Strawberry +<span class="item__dots"></span><span class="item__price">$4.50</span></div><p class="item__desc">Fire roasted marshmello &amp; nocciella</p></div>
    <div class="item"><div class="item__line">Strawberry +<span class="item__dots"></span><span class="item__price">$4.50</span></div><p class="item__desc">Fire roasted marshmello &amp; nocciella</p></div>
    <div class="item"><div class="item__line">Banana + Strawberry +<span class="item__dots"></span><span class="item__price">$4.50</span></div><p class="item__desc">Fire roasted marshmello &amp; nocciella</p></div>
    <div class="item"><div class="item__line">Wild Berries +<span class="item__dots"></span><span class="item__price">$4.50</span></div><p class="item__desc">Fire roasted marshmello &amp; nocciella</p></div>
    <div class="item"><div class="item__line">Mixed Fruits +<span class="item__dots"></span><span class="item__price">$4.50</span></div><p class="item__desc">Fire roasted marshmello &amp; nocciella</p></div>
    <div class="item"><div class="item__line">Peanut Butter + Banana +<span class="item__dots"></span><span class="item__price">$4.50</span></div><p class="item__desc">Fire roasted marshmello &amp; nocciella</p></div>
    <div class="item"><div class="item__line">Cinnamon + Apple + Brown Sugar +<span class="item__dots"></span><span class="item__price">$4.50</span></div><p class="item__desc">Fire roasted marshmello &amp; nocciella</p></div>
  </div>

  <footer class="footer">
    <div class="footer__texture" role="img" aria-label="Light grey wood texture with faint line drawings of cooking ingredients"></div>
    <svg class="footer__wave" viewBox="0 0 518 34" preserveAspectRatio="none" aria-hidden="true">
      <path d="M0 0 L518 0 L518 14 C440 20 360 6 260 8 C160 10 70 24 0 14Z" fill="var(--paper)"/>
      <path d="M0 14 C70 24 160 10 260 8 C360 6 440 20 518 14 L518 18 C440 24 360 11 260 13 C160 15 70 28 0 20Z" fill="var(--red)"/>
      <path d="M0 20 C70 28 160 15 260 13 C360 11 440 24 518 18 L518 20 C440 26 360 14 260 16 C160 18 70 30 0 23Z" fill="#222"/>
    </svg>
  </footer>
</section>

</body>
</html>
```